Zielgruppe
Wir produzieren Rebuilt Toner Kartuschen und vertreiben diese an privat Anwender und auch Firmen Kunden.
Unsere Produkte vertreiben wir unter einer eigenen Marke und auch neutral an Wiederverkäufer.
Jetzt suchen wir ein neues Produkt Aufkleber Design für die neutrale Ware (ohne Logo) soll aber trotzdem ein Wiedererkennungswert haben, aber nicht direkt auf uns zurückführen.
Ein Bild vom aktuellen Aufkleber, ist anbei.
Aufgabenstellung
Es soll ein universal Design sein welches wir für alle Produkte verwenden können. Somit keine Artikel Informationen im Design.
Als Text soll 'Rebuilt Cartridge' und 'Made in Germany' verwendet werden.
Das Design soll die hohe Qualität unterstreichen.
Die Hintergrundfarbe soll Schwarz sein.
Der Standard Aufkleber soll die Abmessungen 233x84mm haben.

```html
<!DOCTYPE html>
<html lang="de">
<head>
<meta charset="utf-8">
<title>Rebuilt Cartridge – Produktaufkleber</title>
<link rel="stylesheet" href="https://fonts.googleapis.com/css2?family=Great+Vibes&family=Roboto:wght@300&display=swap">
<style>
  :root {
    --label-black: #000000;
    --label-white: #ffffff;
    --page-bg: #ffffff;
  }
  html, body {
    margin: 0;
    padding: 0;
    width: 1200px;
    height: 454px;
    overflow: hidden;
    background: var(--page-bg);
  }
  .sticker {
    display: block;
    width: 1200px;
    height: 454px;
  }
  .sticker__base { fill: var(--label-black); }
  .sticker__frame,
  .sticker__corner {
    fill: none;
    stroke: var(--label-white);
    stroke-width: 7;
    stroke-linejoin: miter;
  }
  .sticker__script {
    font-family: "Great Vibes", cursive;
    fill: var(--label-white);
  }
  .sticker__title {
    font-family: "Roboto", sans-serif;
    font-weight: 300;
    fill: var(--label-white);
    letter-spacing: 1px;
  }
</style>
</head>
<body>
<svg class="sticker" viewBox="0 0 1200 454" xmlns="http://www.w3.org/2000/svg">
  <rect class="sticker__base" x="21" y="18" width="1158" height="418"/>
  <polygon class="sticker__frame" points="46,43 1156,43 1156,264 960,411 46,411"/>
  <polygon class="sticker__corner" points="1156,289 1156,411 1004,411"/>

  <text class="sticker__script" x="566" y="136" font-size="44" text-anchor="middle">Premium</text>
  <text class="sticker__title" x="566" y="248" font-size="68" text-anchor="middle"
        textLength="692" lengthAdjust="spacingAndGlyphs">REBUILT CARTRIDGE</text>
  <text class="sticker__script" x="570" y="336" font-size="58" text-anchor="middle">Made in Germany</text>
</svg>
</body>
</html>
```